Copperfield Provisions Company Label

I need a label designed that will reflect the Copperfield Provisions Company. We produce and source locally meat products such as sausages, pates, terrines, mousses etc.... The label needs to communicate artistry, modernism, hand made, playfulness. We produce the finest meat products and utilize only locally sourced meat from the best farmers. All these things we hold in high regard and it needs to be reflected in the label. The label must also have a vintage feel since we are using vintage techniques of production. The first image file is my companies logo and should be used as a jumping off point.
Should be no larger then 4"x 4", I dont have specifics on shape i am open to anything. The packaging is ROP (reduced oxygen packaging) sometimes called cyo-vac packaging.
Please yield to the images i posted as inspiration in the direction i want. The logo does not have to be used, but i would like it in the same vein of design. Again artistry and graphics.
Target Market(s)
Consumer who care about the products they are consuming. These people frequent farmers markets and have a tend to buy locally even when it is more expensive.
Industry/Entity Type
It Company
Requirements
Must have
- Vintage imagery and a modern feel, a red and black color scheme. Other colors will be acceptable in the right taste. A statement of weight, use any for this case. Must have a place for the contents of the package, "Grass Fed Hot Dogs" for example.
Nice to have
- A old timely friendly butcher, a hand crank meat grinder, wooden butcher tables, cleavers.
Should not have
- Animal silhouettes

```html
<!DOCTYPE html>
<html lang="en">
<head>
<meta charset="utf-8">
<title>Copperfield Provisions Company – Label Set</title>
<link rel="stylesheet" href="https://fonts.googleapis.com/css2?family=Lobster&family=Oswald:wght@400;600;700&family=Montserrat:wght@600;700&display=swap">
<style>
  :root{
    --coal:#2b2827;
    --flame:#ef3b2c;
    --crimson:#c8102e;
    --bone:#e7e6e4;
    --rim:#343232;
    --white:#ffffff;
    --steel:#b9b7b4;
  }
  html,body{margin:0;padding:0;overflow:hidden;}
  body{width:1200px;height:1200px;background:var(--white);position:relative;}
  .label{position:absolute;width:520px;height:520px;}
  .label--coal-flame{left:96px;top:70px;}
  .label--flame{left:602px;top:70px;}
  .label--coal-crimson{left:85px;top:620px;}
  .label--crimson{left:602px;top:620px;}
  .est{font-family:"Montserrat",sans-serif;font-weight:600;font-size:15px;letter-spacing:3px;}
  .tagline{font-family:"Montserrat",sans-serif;font-weight:700;font-size:12px;letter-spacing:1px;}
  .tagline-script{font-family:"Lobster",cursive;font-size:17px;}
  .name-script{font-family:"Lobster",cursive;font-size:36px;}
  .name-block{font-family:"Oswald",sans-serif;font-weight:700;font-size:52px;}
  .company{font-family:"Oswald",sans-serif;font-weight:400;font-size:18px;letter-spacing:4px;}
  .contents{font-family:"Montserrat",sans-serif;font-weight:700;font-size:14px;}
  .weight{font-family:"Oswald",sans-serif;font-weight:400;font-size:18px;letter-spacing:2px;}
</style>
</head>
<body>

<!-- Label 1: coal field, flame accents, cleaver artwork -->
<svg class="label label--coal-flame" viewBox="-260 -260 520 520">
  <defs>
    <path id="arc-a" d="M -70 -150 Q 0 -185 70 -150"/>
    <linearGradient id="band-a" x1="0" x2="1"><stop offset="0" stop-color="#2b2827"/><stop offset=".5" stop-color="#9a9896"/><stop offset="1" stop-color="#2b2827"/></linearGradient>
  </defs>
  <polygon points="0,-250 250,0 0,250 -250,0" fill="var(--bone)" stroke="var(--rim)" stroke-width="5" stroke-linejoin="round"/>
  <polygon points="0,-230 230,0 0,230 -230,0" fill="var(--coal)" stroke-linejoin="round"/>
  <text class="est" fill="var(--white)" text-anchor="middle"><textPath href="#arc-a" startOffset="50%">EST. 1999</textPath></text>
  <g role="img" aria-label="Two crossed butcher cleavers beneath a small sunburst">
    <rect x="-75" y="-135" width="150" height="85" rx="14" fill="#6f6c6a"/>
  </g>
  <line x1="-150" y1="-58" x2="-70" y2="-58" stroke="var(--white)" stroke-width="1.5"/>
  <line x1="70" y1="-58" x2="150" y2="-58" stroke="var(--white)" stroke-width="1.5"/>
  <text class="tagline" x="-110" y="-42" fill="var(--white)" text-anchor="middle">LOCALLY</text>
  <text class="tagline" x="110" y="-42" fill="var(--white)" text-anchor="middle">PRODUCED</text>
  <text class="name-script" x="0" y="0" fill="var(--flame)" text-anchor="middle" textLength="340" lengthAdjust="spacingAndGlyphs">Copperfield Provisions</text>
  <polygon points="-105,20 105,20 95,38 105,56 -105,56 -95,38" fill="none" stroke="var(--white)" stroke-width="1.5"/>
  <text class="company" x="0" y="45" fill="var(--white)" text-anchor="middle">COMPANY</text>
  <polygon points="-150,65 150,65 140,82 -140,82" fill="url(#band-a)"/>
  <text class="contents" x="0" y="107" fill="var(--flame)" text-anchor="middle">GRASS FED HOTDOGS</text>
  <polygon points="-100,120 100,120 80,150 -80,150" fill="url(#band-a)"/>
  <polygon points="-32,160 32,160 40,180 0,210 -40,180" fill="var(--flame)"/>
  <text class="weight" x="0" y="188" fill="var(--coal)" text-anchor="middle">1 LB</text>
</svg>

<!-- Label 2: flame field, coal accents, cleaver artwork -->
<svg class="label label--flame" viewBox="-260 -260 520 520">
  <defs>
    <path id="arc-b" d="M -70 -150 Q 0 -185 70 -150"/>
    <linearGradient id="band-b" x1="0" x2="1"><stop offset="0" stop-color="#ef3b2c"/><stop offset=".5" stop-color="#5a2521"/><stop offset="1" stop-color="#ef3b2c"/></linearGradient>
  </defs>
  <polygon points="0,-250 250,0 0,250 -250,0" fill="var(--bone)" stroke="var(--rim)" stroke-width="5" stroke-linejoin="round"/>
  <polygon points="0,-230 230,0 0,230 -230,0" fill="var(--flame)"/>
  <text class="est" fill="var(--coal)" text-anchor="middle"><textPath href="#arc-b" startOffset="50%">EST. 1999</textPath></text>
  <g role="img" aria-label="Two crossed butcher cleavers beneath a small sunburst">
    <rect x="-75" y="-135" width="150" height="85" rx="14" fill="#c9c2bf"/>
  </g>
  <line x1="-150" y1="-58" x2="-70" y2="-58" stroke="var(--coal)" stroke-width="1.5"/>
  <line x1="70" y1="-58" x2="150" y2="-58" stroke="var(--coal)" stroke-width="1.5"/>
  <text class="tagline" x="-110" y="-42" fill="var(--coal)" text-anchor="middle">LOCALLY</text>
  <text class="tagline" x="110" y="-42" fill="var(--coal)" text-anchor="middle">PRODUCED</text>
  <text class="name-script" x="0" y="0" fill="var(--coal)" text-anchor="middle" textLength="340" lengthAdjust="spacingAndGlyphs">Copperfield Provisions</text>
  <polygon points="-105,20 105,20 95,38 105,56 -105,56 -95,38" fill="none" stroke="var(--bone)" stroke-width="1.5"/>
  <text class="company" x="0" y="45" fill="var(--coal)" text-anchor="middle">COMPANY</text>
  <polygon points="-150,65 150,65 140,82 -140,82" fill="url(#band-b)"/>
  <text class="contents" x="0" y="107" fill="var(--coal)" text-anchor="middle">GRASS FED HOTDOGS</text>
  <polygon points="-100,120 100,120 80,150 -80,150" fill="url(#band-b)"/>
  <polygon points="-32,160 32,160 40,180 0,210 -40,180" fill="var(--bone)"/>
  <text class="weight" x="0" y="188" fill="var(--coal)" text-anchor="middle">1 LB</text>
</svg>

<!-- Label 3: coal field, crimson rim, butcher artwork -->
<svg class="label label--coal-crimson" viewBox="-260 -260 520 520">
  <defs>
    <path id="arc-c" d="M -60 -158 Q 0 -188 60 -158"/>
    <linearGradient id="band-c" x1="0" x2="1"><stop offset="0" stop-color="#2b2827"/><stop offset=".5" stop-color="#9a9896"/><stop offset="1" stop-color="#2b2827"/></linearGradient>
  </defs>
  <polygon points="0,-252 252,0 0,252 -252,0" fill="var(--crimson)" stroke="var(--crimson)" stroke-width="8" stroke-linejoin="round"/>
  <polygon points="0,-232 232,0 0,232 -232,0" fill="var(--coal)"/>
  <text class="est" fill="var(--white)" text-anchor="middle"><textPath href="#arc-c" startOffset="50%">EST. 1999</textPath></text>
  <g role="img" aria-label="Friendly butcher in a striped apron holding a cleaver, with a sunburst behind">
    <rect x="-65" y="-148" width="130" height="100" rx="16" fill="#d8d6d3"/>
  </g>
  <line x1="-140" y1="-38" x2="-75" y2="-38" stroke="var(--crimson)" stroke-width="1.5"/>
  <line x1="75" y1="-38" x2="140" y2="-38" stroke="var(--crimson)" stroke-width="1.5"/>
  <text class="tagline-script" x="-105" y="-44" fill="var(--crimson)" text-anchor="middle">Locally</text>
  <text class="tagline-script" x="105" y="-44" fill="var(--crimson)" text-anchor="middle">Produced</text>
  <text class="name-block" x="0" y="22" fill="var(--bone)" text-anchor="middle" textLength="400" lengthAdjust="spacingAndGlyphs">COPPERFIELD PROVISIONS</text>
  <polygon points="-105,32 105,32 95,48 105,64 -105,64 -95,48" fill="var(--crimson)"/>
  <text class="company" x="0" y="55" fill="var(--coal)" text-anchor="middle">COMPANY</text>
  <polygon points="-140,75 140,75 130,92 -130,92" fill="url(#band-c)"/>
  <text class="contents" x="0" y="116" fill="var(--crimson)" text-anchor="middle">GRASS FED HOTDOGS</text>
  <polygon points="-95,128 95,128 75,156 -75,156" fill="url(#band-c)"/>
  <polygon points="-32,164 32,164 40,184 0,212 -40,184" fill="var(--crimson)"/>
  <text class="weight" x="0" y="191" fill="var(--coal)" text-anchor="middle">1 LB</text>
</svg>

<!-- Label 4: crimson field, butcher artwork -->
<svg class="label label--crimson" viewBox="-260 -260 520 520">
  <defs>
    <path id="arc-d" d="M -60 -158 Q 0 -188 60 -158"/>
    <linearGradient id="band-d" x1="0" x2="1"><stop offset="0" stop-color="#c8102e"/><stop offset=".5" stop-color="#5a1a24"/><stop offset="1" stop-color="#c8102e"/></linearGradient>
  </defs>
  <polygon points="0,-250 250,0 0,250 -250,0" fill="var(--bone)" stroke="var(--rim)" stroke-width="5" stroke-linejoin="round"/>
  <polygon points="0,-230 230,0 0,230 -230,0" fill="var(--crimson)"/>
  <text class="est" fill="var(--white)" text-anchor="middle"><textPath href="#arc-d" startOffset="50%">EST. 1999</textPath></text>
  <g role="img" aria-label="Friendly butcher in a striped apron holding a cleaver, with a sunburst behind">
    <rect x="-65" y="-148" width="130" height="100" rx="16" fill="#e3c9cd"/>
  </g>
  <line x1="-140" y1="-38" x2="-75" y2="-38" stroke="var(--coal)" stroke-width="1.5"/>
  <line x1="75" y1="-38" x2="140" y2="-38" stroke="var(--coal)" stroke-width="1.5"/>
  <text class="tagline-script" x="-105" y="-44" fill="var(--coal)" text-anchor="middle">Locally</text>
  <text class="tagline-script" x="105" y="-44" fill="var(--coal)" text-anchor="middle">Produced</text>
  <text class="name-block" x="0" y="22" fill="#111" text-anchor="middle" textLength="400" lengthAdjust="spacingAndGlyphs">COPPERFIELD PROVISIONS</text>
  <polygon points="-105,32 105,32 95,48 105,64 -105,64 -95,48" fill="var(--bone)"/>
  <text class="company" x="0" y="55" fill="var(--coal)" text-anchor="middle">COMPANY</text>
  <polygon points="-140,75 140,75 130,92 -130,92" fill="url(#band-d)"/>
  <text class="contents" x="0" y="116" fill="var(--coal)" text-anchor="middle">GRASS FED HOTDOGS</text>
  <polygon points="-95,128 95,128 75,156 -75,156" fill="url(#band-d)"/>
  <polygon points="-32,164 32,164 40,184 0,212 -40,184" fill="var(--bone)"/>
  <text class="weight" x="0" y="191" fill="var(--coal)" text-anchor="middle">1 LB</text>
</svg>

</body>
</html>
```